Website Redesign - Mobile Friendly tour operator site required

We have a current website at http://www.quillmerevoyages.com. The UI needs an overhaul to make it mobile friendly and modern design with good integration with Social Media. The site is currently running .net and all the content is being driven from the backend database managed through our CMS.
Our goal in this project is to just get the bootstrap with upgraded UI that will encompass all the aspects of the existing content. For example - there are multiple pieces in the tour - Itinerary, Calendar, tour map, Accommodation details, city details, photo gallery, testimonials, places for upsell, promotions, video download, brochures etc. - So the design has to be made keeping in mind the existing content objects. Placement of these can be changed to ensure that the pages deliver a visible Click-to-Action for tour bookings / lead genertion etc.

Essentially there are the following templates / pages that need to be redesigned -
Tour Page : Example : http://www.quillmerevoyages.com/tours-el-marbeno-velvet-crown-rail-train-journey-from-seville-t706.aspx
Tour List Page : Example : http://www.quillmerevoyages.com/TourList1.aspx?catid=76&rid=11
Country Page : Example - http://www.quillmerevoyages.com/default.aspx?rid=11
Category Page : Example - http://www.quillmerevoyages.com/TourList1.aspx?catid=76&rid=11
and the Home Page

The Navigation of the site is generated dynamically so for the purposes of this project the navigation structure may stay the same. The main goal is to have a mobile friendly site that will be accommodate all the variables driving the content at this time. Placement of these variables in order to accommodate the responsive layout as well as clear call-to-action is what is important. We have videos and a number of images that we can put in a tour so it needs to be less restrictive design - infact it needs to be expandable to accommodate different variations (eg. some tours may have more pictures than other and they need to be accommodated).

The deliverable is a designed front end that when approved will be supported with bootstrap that we will plug our content to. So first the wireframe then CSS/JS and deliverable "slices".

PLEASE - Do NOT give wordpress site. This is a UI design project!

Reason: I got a number of designs and some designers are almost at last stages it seems (I have given feedback to them!) but they need more time to show the layout.

Target Market(s)

B2C Market for travelers.

Industry/Entity Type

Travel

Coding

Coded - Design and coding required

Number of Pages Required

5+ page

Requirements
Must have
• Responsive mobile friendly design
• Ideally have the same color coding as the current design.
• Clearly Visible Integration with Social Media content / links
• Clear Call to Action
• Image Sliders for top of the tour description pages.
• SEO Friendly design
Nice to have
• We have a number of pictures that come in different sizes and cropping / resizing images takes away the impact of the picture . A design that may accommodate the different size images without much "retouching".
Should not have
• No cut-and-dry wordpress templates please!

```html
<!DOCTYPE html>
<html lang="en">
<head>
<meta charset="utf-8">
<title>Quillmere Voyages – Tour Page</title>
<link href="https://fonts.googleapis.com/css2?family=Open+Sans:wght@400;600;700&family=Oswald:wght@400;500&display=swap" rel="stylesheet">
<style>
:root{
  --red:#7d0f1c;
  --red-dark:#5a0812;
  --red-bright:#a3172a;
  --ink:#222;
  --text:#555;
  --muted:#888;
  --dark:#1f1f1f;
  --darker:#151515;
  --light:#f1f1f1;
  --line:#ddd;
  --white:#fff;
}
*{box-sizing:border-box;margin:0;padding:0}
html,body{width:1200px;height:3400px;overflow:hidden}
body{font-family:"Open Sans",Arial,sans-serif;font-size:13px;color:var(--text);background:var(--white);line-height:1.6}
h1,h2,h3,h4{font-family:"Oswald",Arial,sans-serif;font-weight:400;color:var(--ink);text-transform:uppercase;letter-spacing:.5px}
.wrap{width:1000px;margin:0 auto;position:relative}
.img{display:block}

/* header */
.topbar{height:112px;background:linear-gradient(var(--red),var(--red-dark))}
.topbar .wrap{display:flex;align-items:center;justify-content:space-between;height:112px}
.brand{display:flex;align-items:center;gap:12px;color:var(--white);font-family:"Open Sans",sans-serif;font-weight:700;font-size:20px;letter-spacing:1px}
.brand-dot{width:40px;height:40px;border-radius:50%;background:var(--white);opacity:.9}
.top-actions{display:flex;align-items:center;gap:20px;color:var(--white);font-size:13px;font-weight:600}
.btn-quote{border:1px solid rgba(255,255,255,.6);padding:8px 16px;font-size:11px;letter-spacing:1px;background:var(--red-dark)}
.nav{height:56px;background:#2a2a2a;border-bottom:3px solid var(--red)}
.nav ul{list-style:none;display:flex;height:56px;width:1000px;margin:0 auto}
.nav li{display:flex;align-items:center;padding:0 18px;color:#ddd;font-family:"Oswald",sans-serif;font-size:13px;text-transform:uppercase}
.nav li.active{background:#c8b98a;color:var(--ink)}

/* hero */
.hero{height:512px;position:relative;background:linear-gradient(180deg,#3a2a2e 0%,#b9753e 45%,#e9b06a 62%,#5b3524 100%)}
.hero-caption{position:absolute;left:0;right:0;bottom:60px;text-align:center}
.hero-caption h1{color:var(--white);font-size:40px;letter-spacing:1px}
.hero-caption p{color:#eee;font-size:15px}
.arrow{position:absolute;top:50%;width:40px;height:60px;margin-top:-30px;background:rgba(0,0,0,.45);display:flex;align-items:center;justify-content:center}
.arrow.left{left:0}.arrow.right{right:0}

/* intro */
.intro{height:340px;padding-top:50px}
.intro .wrap{display:flex;gap:40px}
.intro-text{flex:1}
.intro-text h2{font-size:22px;line-height:1.35;margin-bottom:14px}
.intro-text p{margin-bottom:12px}
.btn{display:inline-block;padding:9px 22px;font-size:11px;font-weight:700;color:var(--white);text-transform:uppercase;letter-spacing:1px;margin-right:8px}
.btn-dark{background:var(--ink)}.btn-red{background:var(--red)}
.calendar{width:280px}
.cal-tabs{display:flex;font-size:11px;font-weight:700;text-transform:uppercase}
.cal-tabs span{padding:7px 14px;background:#ddd;color:var(--ink)}
.cal-tabs span.on{background:var(--red);color:var(--white)}
.cal-box{background:var(--red);color:var(--white);padding:12px}
.cal-head{text-align:center;font-weight:700;font-size:12px;margin-bottom:8px}
.cal-grid{display:grid;grid-template-columns:repeat(7,1fr);gap:2px;font-size:11px;text-align:center}
.cal-grid span{padding:4px 0;background:rgba(255,255,255,.08)}
.cal-grid span.d{background:none;font-weight:700}
.cal-grid span.sel{background:var(--white);color:var(--red)}

/* accommodation */
.section-dark{background:var(--dark);color:#bbb}
.section-title{text-align:center;font-size:22px;padding:36px 0 26px}
.section-dark .section-title{color:var(--white)}
.accommodation{height:440px}
.acc-cards{display:flex;gap:40px;justify-content:center}
.acc-card{width:300px;background:#2b2b2b}
.acc-label{background:var(--red);color:var(--white);text-align:center;font-family:"Oswald",sans-serif;font-size:13px;padding:6px;text-transform:uppercase}
.acc-card .img{height:130px}
.acc-card p{padding:14px 16px 0;font-size:12px;text-align:center}

/* itinerary */
.itinerary{height:300px;background:var(--light)}
.itinerary .section-title{padding:26px 0 18px}
.days{display:flex;justify-content:space-between;position:relative}
.days:before{content:"";position:absolute;left:70px;right:70px;top:46px;border-top:2px dotted #bbb}
.day{width:140px;text-align:center;position:relative}
.day h4{font-size:13px;margin-bottom:6px}
.day .img{width:62px;height:62px;border-radius:50%;margin:0 auto 10px;border:3px solid #c89a4a}
.day p{font-size:11px;line-height:1.5}
.day p b{color:var(--red)}

/* gallery */
.gallery{height:340px}
.gallery-row{display:flex;gap:10px;justify-content:center}
.gallery-row .img{width:158px;height:150px}

/* promotions */
.promotions{height:360px;padding-top:44px}
.promotions .wrap{display:flex;gap:40px}
.promo-text{flex:1}
.promo-text h2{font-size:22px;margin-bottom:8px}
.promo-text h3{color:var(--red);font-size:17px;line-height:1.4;margin-bottom:12px}
.promo-video{width:320px;height:200px;position:relative}
.play{position:absolute;left:50%;top:50%;margin:-26px 0 0 -26px}

/* upsell */
.upsell{height:460px;background:var(--light)}
.upsell .section-title{padding:30px 0 8px}
.upsell-intro{text-align:center;font-size:12px;width:800px;margin:0 auto 24px}
.upsell-cards{display:flex;gap:22px;justify-content:center;position:relative}
.up-card{width:232px;background:var(--white);border-bottom:3px solid var(--red)}
.up-card .img{height:150px}
.up-card h4{color:var(--red);font-size:15px;text-transform:none;padding:12px 14px 4px}
.up-card p{font-size:12px;padding:0 14px 16px}
.up-arrow{position:absolute;top:80px;width:24px;height:24px;border-radius:50%;background:var(--ink);display:flex;align-items:center;justify-content:center}

/* bottom info */
.info{height:320px;padding-top:34px}
.info .wrap{display:flex;gap:40px}
.info-col{flex:1}
.info-col h3{font-size:20px;border-bottom:2px solid var(--line);padding-bottom:8px;margin-bottom:16px}
.city-list{list-style:none}
.city-list li{font-size:12px;padding:5px 0 5px 18px;position:relative}
.city-list li:before{content:"";position:absolute;left:0;top:11px;width:8px;height:8px;background:var(--red)}
.quote{border:1px solid var(--line);padding:14px;font-size:12px;font-style:italic;margin-bottom:14px}
.person{display:flex;align-items:center;gap:12px;font-weight:700;color:var(--ink)}
.avatar{width:48px;height:48px;border-radius:50%;background:#9a8a7c}
.brochure{display:flex;gap:12px;margin-bottom:14px}
.b-icon{width:38px;height:38px;background:var(--red);flex:none;display:flex;align-items:center;justify-content:center}
.brochure p{font-size:12px;line-height:1.5}

/* footer */
.footer{height:160px;background:var(--darker);color:#999;font-size:11px;padding-top:30px}
.footer .wrap{display:flex;gap:40px}
.footer .col{flex:1}
.footer h4{color:var(--white);font-size:13px;margin-bottom:8px}
.copy{color:var(--red-bright);margin-bottom:12px}
.socials{display:flex;gap:6px}
.socials span{width:22px;height:22px;background:#444}
</style>
</head>
<body>

<header class="topbar">
  <div class="wrap">
    <div class="brand"><span class="brand-dot"></span>Quillmere Voyages</div>
    <div class="top-actions">
      <span>CALL US : +44 (0) 20 3948 6120</span>
      <span class="btn-quote">REQUEST A QUOTE</span>
    </div>
  </div>
</header>
<nav class="nav">
  <ul>
    <li class="active">Home</li><li>Luxury Trains</li><li>Group Tours</li><li>Independent / Other Tours</li><li>Transfers</li><li>Rail Passes</li><li>Rent a Car</li><li>Contact Us</li>
  </ul>
</nav>

<section class="hero" role="img" aria-label="Evening photograph of a grand plaza and palace in Seville">
  <div class="arrow left"><svg width="14" height="22"><path d="M11 2 3 11l8 9" stroke="#fff" stroke-width="2.5" fill="none"/></svg></div>
  <div class="arrow right"><svg width="14" height="22"><path d="M3 2l8 9-8 9" stroke="#fff" stroke-width="2.5" fill="none"/></svg></div>
  <div class="hero-caption">
    <h1>Tour the Gorgeous City of Seville</h1>
    <p>Lorem ipsum dolor sit amet, consectetuer adipiscing elit.</p>
  </div>
</section>

<section class="intro">
  <div class="wrap">
    <div class="intro-text">
      <h2>El Marbeno Velvet Crown Rail Train Journey<br>from Seville</h2>
      <p>In 2015 the El Marbeno Velvet Crown Rail train will run its classic 7 day package and will have an extra route in Seville. Journeys are offered from April to October, with departures every week and a choice of cabin categories throughout the season.</p>
      <p>Discover and experience the breathtaking landscapes of Southern Spain aboard this luxurious travelling hotel, with stops at Córdoba, Granada, Ronda and Jerez before returning to Seville in great comfort.</p>
      <p>This sparkling 6 day journey takes you through some of Spain's most beautiful cities and monuments in the elegance of a restored classic train.</p>
      <span class="btn btn-dark">Read More</span><span class="btn btn-red">Contact Now</span>
    </div>
    <aside class="calendar">
      <div class="cal-tabs"><span class="on">Calendar</span><span>Tour Map</span></div>
      <div class="cal-box">
        <div class="cal-head">AUGUST 2015</div>
        <div class="cal-grid">
          <span class="d">S</span><span class="d">M</span><span class="d">T</span><span class="d">W</span><span class="d">T</span><span class="d">F</span><span class="d">S</span>
          <span></span><span></span><span></span><span></span><span></span><span></span><span>1</span>
          <span>2</span><span>3</span><span>4</span><span>5</span><span>6</span><span>7</span><span>8</span>
          <span>9</span><span>10</span><span>11</span><span>12</span><span class="sel">13</span><span>14</span><span>15</span>
          <span>16</span><span>17</span><span>18</span><span>19</span><span>20</span><span>21</span><span>22</span>
          <span>23</span><span>24</span><span>25</span><span>26</span><span>27</span><span>28</span><span>29</span>
          <span>30</span><span>31</span><span></span><span></span><span></span><span></span><span></span>
        </div>
      </div>
    </aside>
  </div>
</section>

<section class="section-dark accommodation">
  <h2 class="section-title">Accommodation</h2>
  <div class="acc-cards">
    <div class="acc-card"><div class="acc-label">Sevilla</div><div class="img" role="img" aria-label="Photograph of a Seville hotel" style="background:linear-gradient(#7a4a36,#c9925a)"></div><p>Ut wisi enim ad minim veniam, quis nostrud exerci tation ullamcorper suscipit lobortis nisl ut aliquip ex ea commodo.</p></div>
    <div class="acc-card"><div class="acc-label">Sevilla – Plaza España</div><div class="img" role="img" aria-label="Photograph of Plaza de España" style="background:linear-gradient(#6d8db8,#c99a6a)"></div><p>Lorem ipsum dolor sit amet, consectetuer adipiscing elit, sed diam nonummy nibh euismod tincidunt ut laoreet.</p></div>
    <div class="acc-card"><div class="acc-label">Córdoba Mezquita</div><div class="img" role="img" aria-label="Photograph of the Córdoba Mezquita arches" style="background:linear-gradient(#8a3a28,#d6a66a)"></div><p>Nam liber tempor cum soluta nobis eleifend option congue nihil imperdiet doming id quod mazim placerat.</p></div>
  </div>
</section>

<section class="itinerary">
  <h2 class="section-title">Tour – Itinerary</h2>
  <div class="wrap days">
    <div class="day"><h4>Day 1</h4><div class="img" role="img" aria-label="Seville station" style="background:#8c6a4a"></div><p>Board the train in Seville, welcome dinner on board.<br><b>Seville</b></p></div>
    <div class="day"><h4>Day 2</h4><div class="img" role="img" aria-label="Jerez bodega" style="background:#a47a4e"></div><p>Morning visit to Jerez and a sherry tasting.<br><b>Jerez – Cádiz</b></p></div>
    <div class="day"><h4>Day 3</h4><div class="img" role="img" aria-label="Ronda gorge" style="background:#7a6a5a"></div><p>Visit Ronda, the old bridge and the bullring.<br><b>Ronda</b></p></div>
    <div class="day"><h4>Day 4</h4><div class="img" role="img" aria-label="Alhambra in Granada" style="background:#b0784a"></div><p>Granada, home of the Alhambra palace.<br><b>Granada</b></p></div>
    <div class="day"><h4>Day 5</h4><div class="img" role="img" aria-label="Baeza old town" style="background:#9a5a3a"></div><p>Visit Baeza and Úbeda, then travel on.<br><b>Baeza – Úbeda</b></p></div>
    <div class="day"><h4>Day 6</h4><div class="img" role="img" aria-label="Córdoba mosque" style="background:#8a4a2e"></div><p>Tour of Córdoba and return to Seville.<br><b>Córdoba – Seville</b></p></div>
  </div>
</section>

<section class="section-dark gallery">
  <h2 class="section-title">Photo Gallery</h2>
  <div class="gallery-row">
    <div class="img" role="img" aria-label="Train exterior" style="background:linear-gradient(#4a3a30,#8a6a4a)"></div>
    <div class="img" role="img" aria-label="Dining carriage" style="background:linear-gradient(#6a2a1a,#c7844a)"></div>
    <div class="img" role="img" aria-label="Lounge carriage" style="background:linear-gradient(#5a1e14,#b8703c)"></div>
    <div class="img" role="img" aria-label="Bar carriage" style="background:linear-gradient(#3a2a20,#a0683c)"></div>
    <div class="img" role="img" aria-label="Cabin interior" style="background:linear-gradient(#6a3a22,#d0945a)"></div>
    <div class="img" role="img" aria-label="Restaurant table setting" style="background:linear-gradient(#4a2014,#b07040)"></div>
  </div>
</section>

<section class="promotions">
  <div class="wrap">
    <div class="promo-text">
      <h2>Our Promotions</h2>
      <h3>Lorem ipsum dolor sit amet, consectetuer adipiscing elit, sed diam nonummy nibh</h3>
      <p>Ut wisi enim ad minim veniam, quis nostrud exerci tation ullamcorper suscipit lobortis nisl ut aliquip ex ea commodo consequat. Duis autem vel eum iriure dolor in hendrerit in vulputate velit esse molestie consequat, vel illum dolore eu feugiat nulla facilisis at vero eros et accumsan et iusto odio dignissim qui blandit praesent luptatum zzril delenit augue duis dolore te feugait nulla facilisi.</p>
    </div>
    <div class="promo-video img" role="img" aria-label="Video still of an equestrian statue against the sky" style="background:linear-gradient(#cfd8e2,#8a949c)">
      <svg class="play" width="52" height="52" viewBox="0 0 52 52"><circle cx="26" cy="26" r="25" fill="rgba(0,0,0,.55)"/><path d="M21 16l15 10-15 10z" fill="#fff"/></svg>
    </div>
  </div>
</section>

<section class="upsell">
  <h2 class="section-title">Places for Upsell</h2>
  <p class="upsell-intro">Lorem ipsum dolor sit amet, consectetuer adipiscing elit, sed diam nonummy nibh euismod tincidunt ut laoreet dolore magna aliquam erat volutpat wisi enim.</p>
  <div class="wrap upsell-cards">
    <div class="up-arrow" style="left:-34px"><svg width="10" height="12"><path d="M8 1 2 6l6 5" stroke="#fff" stroke-width="2" fill="none"/></svg></div>
    <div class="up-card"><div class="img" role="img" aria-label="Coastal town photograph" style="background:linear-gradient(#6a9ac0,#c9a878)"></div><h4>Location Name</h4><p>Lorem ipsum dolor sit amet, consectetuer adipiscing elit, sed diam nonummy.</p></div>
    <div class="up-card"><div class="img" role="img" aria-label="Hotel room photograph" style="background:linear-gradient(#7a2a1e,#c27a4a)"></div><h4>Location Name</h4><p>Lorem ipsum dolor sit amet, consectetuer adipiscing elit, sed diam nonummy.</p></div>
    <div class="up-card"><div class="img" role="img" aria-label="Palace interior photograph" style="background:linear-gradient(#8a6a3a,#d6b07a)"></div><h4>Location Name</h4><p>Lorem ipsum dolor sit amet, consectetuer adipiscing elit, sed diam nonummy.</p></div>
    <div class="up-card"><div class="img" role="img" aria-label="Luxury suite photograph" style="background:linear-gradient(#c8b8a0,#8a6a50)"></div><h4>Location Name</h4><p>Lorem ipsum dolor sit amet, consectetuer adipiscing elit, sed diam nonummy.</p></div>
    <div class="up-arrow" style="right:-34px"><svg width="10" height="12"><path d="M2 1l6 5-6 5" stroke="#fff" stroke-width="2" fill="none"/></svg></div>
  </div>
</section>

<section class="info">
  <div class="wrap">
    <div class="info-col">
      <h3>Cities</h3>
      <ul class="city-list">
        <li>Lorem ipsum dolor sit amet, consectetuer adipiscing</li>
        <li>Sed diam nonummy nibh euismod tincidunt</li>
        <li>Ut laoreet dolore magna aliquam erat volutpat</li>
        <li>Ut wisi enim ad minim veniam quis nostrud</li>
        <li>Exerci tation ullamcorper suscipit lobortis nisl</li>
      </ul>
    </div>
    <div class="info-col">
      <h3>Testimonials</h3>
      <div class="quote">Lorem ipsum dolor sit amet, consectetuer adipiscing elit, sed diam nonummy nibh euismod tincidunt ut laoreet dolore magna aliquam erat volutpat.</div>
      <div class="person"><span class="avatar" role="img" aria-label="Customer portrait"></span>John Doe</div>
    </div>
    <div class="info-col">
      <h3>Brochures</h3>
      <div class="brochure"><span class="b-icon"><svg width="16" height="20"><path d="M1 1h10l4 4v14H1z" fill="none" stroke="#fff" stroke-width="1.6"/></svg></span><p>Lorem ipsum dolor sit amet, consectetuer adipiscing elit, sed diam nonummy nibh.</p></div>
      <div class="brochure"><span class="b-icon"><svg width="16" height="20"><path d="M1 1h10l4 4v14H1z" fill="none" stroke="#fff" stroke-width="1.6"/></svg></span><p>Ut wisi enim ad minim veniam, quis nostrud exerci tation ullamcorper suscipit.</p></div>
      <div class="brochure"><span class="b-icon"><svg width="16" height="20"><path d="M1 1h10l4 4v14H1z" fill="none" stroke="#fff" stroke-width="1.6"/></svg></span><p>Duis autem vel eum iriure dolor in hendrerit in vulputate velit esse molestie.</p></div>
    </div>
  </div>
</section>

<footer class="footer">
  <div class="wrap">
    <div class="col">
      <p class="copy">© 2015 Quillmere Voyages. All rights reserved.</p>
      <div class="socials"><span></span><span></span><span></span><span></span><span></span><span></span></div>
    </div>
    <div class="col"><h4>Our Location</h4><p>14 Harrowgate Lane<br>London, W2 4QT<br>United Kingdom</p></div>
    <div class="col"><h4>Keep in Touch</h4><p>Phone: +44 (0) 20 3948 6120<br>Fax: +44 (0) 20 3948 6121<br>hello@quillmerevoyages.com</p></div>
    <div class="col"><h4>Quick Links</h4><p>Luxury Trains · Group Tours<br>Rail Passes · Transfers<br>Rent a Car · Contact Us</p></div>
  </div>
</footer>

</body>
</html>
```